Agrarhandel benötigt Homepage
Zielgruppe
Wir sind ein Agrarhandel mit einem Warenumschlagslager im Sinne eines klassischen Einzelhandels und vertreiben Produkte an Landwirte.
Wir vertreiben folgende Hauptproduktgruppen:
Einzelfuttermittel
wie z.B. Sojaexktraktionsschrot. Die einzelnen Produkte könnten z.B. wie die Futtermittel auf folgender Seite dargestellt werden (https://www.hartlinkorn.eu/de/produkt/bistaluron)
Mischfuttermittel
Hier bieten wir unseren Kunden an, individuelles Mischfutter auf Basis unserer Einzelfuttermittel herzustellen.
Weitere Details und weitere Produktbereiche habe ich in einer Powerpoint-Übersicht dargestellt.
Neben diesen Produkten wollen wir uns als Familienunternehmen selbst vorstellen. Zudem betreiben wir in unserer Familie zusätzlich einen Milchviehbetrieb den wir ebenfalls hervorheben möchten, da wir unseren Kunden gegenüber einerseits als Zulieferer aber auch als Kollege auftreten wollen.
Einzelfuttermittel: Hier können wir durch unsere Unabhängigkeit punkten, da wir nicht abhängig von bestimmten Lieferanten sind und dementsprechend unabhängig beraten können. Wir untersuchen im Vergleich zu unseren Wettbewerben die Qualität der Futtermittel bis ins Detail und können daher eine Transparenz bieten, die Konkurrenten in der Regel nicht bieten können. Unser Warenumschlagsplatz mit moderner Technik ermöglicht es uns äußerst kosteneffizient die Waren umschlagen und ausliefern zu können.
Mischfuttermittel: Auf Basis der vorhandenen Einzelfuttermittel stellen wir je nach Kundenwunsch individuelle Mischfutter her. Wir arbeiten mit offenen Deklarationen, sodass unsere Kunden jederzeit nachvollziehen können, ob auch die Einzelfuttermittel verwendet wurden, die sie bestellt haben und keine billigen Ersatzprodukte verwendet wurden.
Zudem sind wir BZ und TRUM zertifiziert. Die aktuellen für unser Unternehmen ausgestellten Zertifikate müssen für unsere Kunden als Download zur Verfügung stehen. Statt dem TRUM-Logo bitte das ..
Aufgabenstellung
Wir möchten gerne ein zeitgemäße Homepage, jedoch muss auch berücksichtigt werden, dass unsere Kunden eher konservativ denken.

```html
<!DOCTYPE html>
<html lang="de">
<head>
<meta charset="utf-8">
<title>Auental Agrarhandel – Ihr zuverlässiger Partner im Agrarhandel</title>
<link rel="stylesheet" href="https://fonts.googleapis.com/css2?family=DM+Sans:wght@400;500;700&family=Homemade+Apple&display=swap">
<style>
:root{
  --green:#1f7557;
  --green-dark:#17664b;
  --orange:#f5a623;
  --ink:#2b2b2b;
  --muted:#6c6c6c;
  --paper:#ffffff;
  --line:#e4e4e4;
}
*{box-sizing:border-box;margin:0;padding:0}
html,body{width:1200px;height:4647px;overflow:hidden;background:var(--paper)}
body{font-family:"DM Sans",Arial,sans-serif;color:var(--ink);position:relative}
.abs{position:absolute}
.script{font-family:"Homemade Apple",cursive;color:var(--green);font-size:13px;font-weight:400}
.section-title{font-size:32px;line-height:30px;color:var(--green);font-weight:400}
.section-title .script{font-size:13px;margin-left:6px}
.btn{display:inline-block;font-size:12px;letter-spacing:2.5px;text-transform:uppercase;padding:9px 26px;font-weight:500}
.btn-orange{background:var(--orange);color:#3b2a06}
.btn-green{background:var(--green);color:#fff}

.hero{position:absolute;left:0;top:0;width:1200px;height:749px;
  background:linear-gradient(180deg,#eee9e2 0%,#e2d9cc 38%,#a89377 58%,#5e4a35 78%,#3a2d20 100%)}
.nav{position:absolute;top:28px;left:595px;display:flex;gap:26px;font-size:11px;color:#333;text-transform:uppercase}
.nav-cta{position:absolute;top:24px;left:1022px;width:98px;height:26px;background:var(--orange);color:#fff;font-size:11px;text-align:center;line-height:26px}
.nav-brand{position:absolute;top:22px;left:80px;font-size:13px;font-weight:700;color:var(--green);display:flex;align-items:center;gap:8px}
.nav-brand i{width:16px;height:16px;border-radius:50%;background:var(--green);display:block}
.hero-brand{position:absolute;left:78px;top:318px;font-family:"DM Sans",Arial,sans-serif;font-size:44px;font-weight:700;color:var(--green);letter-spacing:.5px;white-space:nowrap}
.hero-tag{position:absolute;left:80px;top:374px;font-family:"Homemade Apple",cursive;font-size:20px;color:#1d5a44;white-space:nowrap}
.hero-rule{position:absolute;left:78px;top:312px;width:1042px;height:2px;background:var(--green)}
.hero-intro{position:absolute;left:814px;top:188px;width:306px;font-size:13px;line-height:16px;color:#2e2e2e}
.hero-photo{position:absolute;left:420px;top:330px;width:780px;height:419px;
  background:radial-gradient(ellipse at 70% 70%,#2d2218 0%,rgba(45,34,24,0) 55%),radial-gradient(ellipse at 20% 80%,#3a2c1f 0%,rgba(58,44,31,0) 45%)}
.side-contact{position:absolute;right:0;top:575px;width:52px}
.side-contact div{height:58px;background:#7a2e14;margin-bottom:3px;display:flex;align-items:center;justify-content:center}
.mouse{position:absolute;left:586px;top:702px;width:26px;height:40px;border:2px solid #f2ede6;border-radius:13px}
.mouse:after{content:"";position:absolute;left:10px;top:8px;width:2px;height:10px;background:#f2ede6}

.card{position:absolute;background:#fff;box-shadow:0 4px 18px rgba(0,0,0,.12)}
.card .ph{position:absolute;left:0;right:0;top:0;height:170px}
.card h3{position:absolute;font-size:23px;font-weight:400;color:var(--green);white-space:nowrap}
.card p{position:absolute;font-size:12px;line-height:14px;color:#333}
.card .arrow{position:absolute;bottom:26px}
.card .tag{position:absolute;top:0;right:0;width:28px;height:26px;background:#3b2a22}
.bar-label{font-size:10px;color:#444;margin-top:8px}
.bar{height:5px;background:#e8e8e8;margin-top:5px;width:248px;position:relative}
.bar b{position:absolute;left:0;top:0;height:5px;background:var(--orange)}

.about-ph1{position:absolute;left:0;top:1457px;width:419px;height:426px;background:linear-gradient(135deg,#4d3a2b,#a87745 55%,#3a2a1e)}
.about-ph2{position:absolute;left:255px;top:1597px;width:345px;height:374px;background:linear-gradient(160deg,#c8c5be,#8a7a66 45%,#5f5549)}
.quality{position:absolute;left:502px;top:1754px;width:175px;height:156px;background:#fff;border-radius:10px;padding:12px 14px;box-shadow:0 3px 12px rgba(0,0,0,.18)}
.quality h4{font-size:12px;color:var(--green);font-weight:500}
.quality p{font-size:8px;line-height:10px;color:#444;margin-top:4px}
.about-text{position:absolute;left:695px;top:1562px;width:414px;font-size:12.5px;line-height:15.5px;color:#333}

.tile{position:absolute;overflow:hidden}
.tile span{position:absolute;left:0;right:0;bottom:0;text-align:center;color:#fff;font-size:23px;padding:10px 0;background:rgba(31,117,87,.35)}
.tile.small span{font-size:22px;background:none;text-align:right;padding-right:20px}

.generator{position:absolute;left:0;top:2883px;width:1200px;height:790px;
  background:radial-gradient(ellipse at 30% 55%,#6b5848 0%,#3e3128 35%,#1f1915 65%,#171310 100%)}
.gen-text{position:absolute;left:735px;top:3166px;width:385px;font-size:12.5px;line-height:16px;color:#fff}

.partner{position:absolute;top:3880px;font-size:32px;font-weight:700;color:#6f6f6f}

.footer{position:absolute;left:0;top:4076px;width:1200px;height:571px;background:var(--green)}
.f-col{position:absolute;top:4282px;color:#fff;font-size:12px;line-height:30px}
.f-col h5{font-size:19px;font-weight:400;line-height:24px;margin-bottom:6px}
.field{position:absolute;left:79px;width:361px;height:38px;background:#fff;font-size:11px;color:#888;padding:11px 12px}
</style>
</head>
<body>

<header class="hero">
  <div class="hero-photo" role="img" aria-label="Rinder auf einer Weide im warmen Abendlicht"></div>
  <div class="nav-brand"><i></i>AUENTAL</div>
  <nav class="nav"><span>Über uns</span><span>Produkte ⌄</span><span>Partner</span><span>Downloads</span><span>Kontakt</span></nav>
  <div class="nav-cta">PREISLISTE</div>
  <div class="hero-rule"></div>
  <div class="hero-brand">AUENTAL AGRARHANDEL</div>
  <div class="hero-tag">Ihr zuverlässiger Partner im Agrarhandel!</div>
  <p class="hero-intro">Entdecken Sie unsere umfassende Palette hochwertiger Produkte für Ihre landwirtschaftlichen Bedürfnisse. Als erfahrener Partner bieten wir nicht nur erstklassige Einzelfuttermittel, sondern auch die Möglichkeit, individuelles Mischfutter nach Ihren Anforderungen zu gestalten.</p>
  <div class="side-contact">
    <div><svg width="24" height="18" viewBox="0 0 24 18"><rect x="1" y="1" width="22" height="16" fill="none" stroke="#fff" stroke-width="2"/><path d="M1 1l11 9 11-9" fill="none" stroke="#fff" stroke-width="2"/></svg></div>
    <div><svg width="14" height="24" viewBox="0 0 14 24"><rect x="1" y="1" width="12" height="22" rx="2" fill="none" stroke="#fff" stroke-width="2"/><circle cx="7" cy="19" r="1.3" fill="#fff"/></svg></div>
    <div><svg width="22" height="22"><circle cx="11" cy="11" r="9" fill="none" stroke="#fff" stroke-width="2"/></svg></div>
  </div>
  <div class="mouse"></div>
</header>

<section>
  <h2 class="section-title abs" style="left:78px;top:828px">Unser<span class="script">Beste &amp; beliebteste</span><br>Highlight-Sortiment</h2>

  <article class="card" style="left:0;top:938px;width:267px;height:380px">
    <div class="tag"></div>
    <div class="ph" role="img" aria-label="Haufen Mischfutter" style="background:radial-gradient(ellipse at 45% 55%,#7c7a4f 0%,#bdb99a 45%,#fff 70%)"></div>
    <h3 style="left:0;top:203px">Rindermix 28 / 4RG</h3>
    <p style="left:0;top:246px;width:240px;font-size:10.5px;line-height:12px">Eiweißreiches Ergänzungsfutter für Mischrationen mit Sojaschrot, einem Viertel Körnermais, einem Viertel Melasseschnitzel und Rapsschrot</p>
    <svg class="arrow" style="left:200px" width="40" height="14"><path d="M0 7h38M31 1l7 6-7 6" fill="none" stroke="var(--orange)" stroke-width="1.6"/></svg>
  </article>

  <article class="card" style="left:287px;top:938px;width:300px;height:380px">
    <div class="tag"></div>
    <div class="ph" role="img" aria-label="Flüssigkeitstank im Gitterrahmen" style="background:radial-gradient(ellipse at 50% 50%,#b9bcbf 0%,#e2e3e4 35%,#fff 60%)"></div>
    <h3 style="left:28px;top:203px">Pflanzenrohglyzerin</h3>
    <p style="left:28px;top:243px;width:210px">80% Pflanzenrohglyzerin. Für zuckerreiche und ausgeglichene</p>
    <svg class="arrow" style="left:232px" width="40" height="14"><path d="M0 7h38M31 1l7 6-7 6" fill="none" stroke="var(--orange)" stroke-width="1.6"/></svg>
  </article>

  <article class="card" style="left:599px;top:911px;width:320px;height:434px">
    <div class="ph" role="img" aria-label="Sojaschrot in Nahaufnahme" style="height:180px;background:linear-gradient(180deg,#d2bea6,#e6d8c6 70%,#f4ede3)"></div>
    <h3 style="left:25px;top:198px">ProvitaSoy</h3>
    <div class="abs" style="left:25px;top:234px">
      <div class="bar-label" style="margin-top:0">Rohprotein 45,2%</div><div class="bar"><b style="width:112px"></b></div>
      <div class="bar-label">Rohfaser 12,2%</div><div class="bar"><b style="width:30px"></b></div>
      <div class="bar-label">Rohfett 3,3%</div><div class="bar"><b style="width:10px"></b></div>
      <div class="bar-label">Zucker &amp; Stärke 15,5%</div><div class="bar"><b style="width:38px"></b></div>
    </div>
    <div class="btn btn-green abs" style="left:54px;top:376px;width:190px;text-align:center">Zum Produkt</div>
  </article>

  <article class="card" style="left:933px;top:938px;width:280px;height:380px">
    <div class="tag"></div>
    <div class="ph" role="img" aria-label="Haufen Rapsschrot" style="background:radial-gradient(ellipse at 50% 58%,#d99d1f 0%,#ecc768 35%,#fff 62%)"></div>
    <h3 style="left:28px;top:203px">ProvitaRap</h3>
    <p style="left:28px;top:243px;width:240px">Das Futterprotein wird effizient genutzt. Gute Futteraufnahme durch gute Schmackhaftigkeit</p>
    <svg class="arrow" style="left:232px" width="40" height="14"><path d="M0 7h38M31 1l7 6-7 6" fill="none" stroke="var(--orange)" stroke-width="1.6"/></svg>
  </article>
</section>

<section>
  <div class="about-ph1" role="img" aria-label="Landwirt vor einem Traktor im Abendlicht"></div>
  <div class="about-ph2" role="img" aria-label="Kühe am Futtertisch im Stall"></div>
  <div class="quality">
    <h4>Premium Qualität</h4>
    <p>Unsere Futtermittel unterliegen strengen Qualitätsprüfungen, bei denen wir keine Kompromisse eingehen. Auf diese Weise stellen wir sicher, dass höchste Standards erfüllt werden und Sie stets Futter von herausragender Qualität für Ihre Tiere erhalten.</p>
  </div>
  <h2 class="section-title abs" style="left:695px;top:1468px">Auental<span class="script">Tradition &amp; Moderne</span><br>Agrarhandel</h2>
  <p class="about-text">Bei Auental Agrarhandel GbR sind wir mehr als nur ein Unternehmen – wir sind eine landwirtschaftliche Familie mit tiefen Wurzeln und einem klaren Blick in die Zukunft. Seit 2001 setzen wir auf Tradition, Qualität und persönliche Beziehungen zu unseren Kunden. Unser Engagement erstreckt sich nicht nur auf den Agrarhandel, sondern auch auf einen eigenen Milchviehbetrieb, den wir mit Hingabe führen. Auf unserer "Über uns" Seite möchten wir Ihnen einen Einblick in unsere Geschichte, Werte und die Menschen hinter Auental Agrarhandel GbR geben. Tauchen Sie ein in unsere Welt, in der die Verbindung von Tradition und Innovation den Grundstein für unseren Erfolg bildet.</p>
  <div class="btn btn-orange abs" style="left:695px;top:1770px">Mehr erfahren</div>
</section>

<section>
  <h2 class="section-title abs" style="left:78px;top:2081px">Unser<span class="script">Vielseitig &amp; Anspruchsvoll</span><br>Sortiment</h2>
  <div class="tile" style="left:79px;top:2166px;width:331px;height:379px;background:linear-gradient(150deg,#c9c0b2,#9a6a44 45%,#5d4a3a)" role="img" aria-label="Kalb beim Trinken aus der Flasche"><span>Flüssigfutter</span></div>
  <div class="tile" style="left:437px;top:2166px;width:332px;height:379px;background:linear-gradient(180deg,#c7c8c4,#8f8a82 50%,#4a3528)" role="img" aria-label="Kuh frisst aus der Hand"><span>Einzelfutter</span></div>
  <div class="tile" style="left:796px;top:2166px;width:325px;height:379px;background:linear-gradient(180deg,#8a7350,#6b4a2c 45%,#5e5a2f)" role="img" aria-label="Rind auf der Weide"><span>Mischfutter</span></div>

  <svg class="abs" style="left:22px;top:2660px" width="40" height="16"><path d="M40 8H2M9 1L2 8l7 7" fill="none" stroke="#333" stroke-width="1.6"/></svg>
  <div class="tile small" style="left:79px;top:2572px;width:242px;height:190px;background:linear-gradient(150deg,#6b4a32,#b58b5c 50%,#5a3e2a)" role="img" aria-label="Saatgut in zwei Händen"><span>Saatgut</span></div>
  <div class="tile small" style="left:347px;top:2572px;width:241px;height:190px;background:linear-gradient(180deg,#9fa9a4,#aab5ae 40%,#7b8a5a)" role="img" aria-label="Siloballen auf einer Wiese"><span>Silofolie</span></div>
  <div class="tile small" style="left:614px;top:2572px;width:241px;height:190px;background:linear-gradient(160deg,#8f8870,#c8c4b2 50%,#6f6850)" role="img" aria-label="Mineraldünger auf Ackerboden"><span>Mineraldünger</span></div>
  <div class="tile small" style="left:881px;top:2572px;width:240px;height:190px;background:linear-gradient(160deg,#6a6a74,#7a3a2c 50%,#4a3a36)" role="img" aria-label="Rinder auf Stallmatten"><span>Stallmatten</span></div>
  <svg class="abs" style="left:1140px;top:2660px" width="40" height="16"><path d="M0 8h38M31 1l7 7-7 7" fill="none" stroke="#333" stroke-width="1.6"/></svg>
</section>

<section class="generator" role="img" aria-label="Rind mit weißem Kopf in Nahaufnahme"></section>
<h2 class="section-title abs" style="left:735px;top:3046px;color:var(--orange)">Unser<span class="script" style="color:var(--orange)">Flexibel &amp; einfach</span><br>Futtergenerator</h2>
<p class="gen-text">Hier haben Sie die Möglichkeit, das Futter ganz nach Ihren Anforderungen und den Bedürfnissen Ihrer Tiere individuell zusammenzustellen. Unser benutzerfreundlicher Generator ermöglicht es Ihnen, präzise Angaben zu den gewünschten Inhaltsstoffen bis hin zu speziellen Ernährungsbedürfnissen zu machen. Mit nur wenigen Klicks erhalten Sie eine maßgeschneiderte Empfehlung für Futter, das höchsten Qualitätsstandards entspricht.</p>
<div class="btn btn-orange abs" style="left:735px;top:3334px">Zum Generator</div>

<section>
  <h2 class="section-title abs" style="left:54px;top:3764px">Unsere<span class="script">Vertrauen &amp; Kompetenz</span><br>Partner &amp; Lieferanten</h2>
  <div class="partner" style="left:96px;font-size:26px">Feldstahl Teile</div>
  <div class="partner" style="left:352px">Kalbina</div>
  <div class="partner" style="left:640px;font-size:26px">Korngrund Saaten</div>
  <div class="partner" style="left:882px;font-size:26px;line-height:30px">Nordhafen<br>Kraftfutter GmbH</div>
</section>

<footer class="footer"></footer>
<div class="abs" style="left:81px;top:4200px;color:#fff;font-size:11px;font-weight:700">AUENTAL AGRARHANDEL</div>
<h2 class="section-title abs" style="left:79px;top:4283px;color:var(--orange)">Bleiben Sie<span class="script" style="color:var(--orange)">E-Mail-Verteiler</span><br>auf dem Laufenden</h2>
<div class="field" style="top:4366px">Ihr Name</div>
<div class="field" style="top:4426px">Ihre E-Mail Adresse</div>
<div class="abs" style="left:79px;top:4488px;font-size:11px;color:#fff;display:flex;gap:6px;align-items:center"><i style="width:9px;height:9px;background:#fff;display:block"></i>Ich akzeptiere die <span style="color:var(--orange)">Datenschutzbestimmungen</span></div>
<div class="btn btn-orange abs" style="left:79px;top:4525px">Absenden</div>

<div class="f-col" style="left:491px"><h5>Kontakt</h5><div style="line-height:14px">Auental Agrarhandel GbR<br>Feldgasse 7<br>84512 Wiesenhall</div><div>+49 9876 5432100</div><div>kontakt@auental-agrar.de</div></div>
<div class="f-col" style="left:686px"><h5>Info</h5>AGB's<br>Datenschutz<br>Impressum<br>Cookie-Hinweis<br>Lieferbedingungen</div>
<div class="f-col" style="left:839px"><h5>Menü</h5>Über uns<br>Produkte +<br>Partner<br>Downloads<br>Kontakt</div>
<div class="f-col" style="left:976px"><h5>Zertifikate</h5>
  <div style="display:flex;gap:10px"><i style="width:60px;height:70px;background:#fff;display:block"></i><i style="width:60px;height:70px;background:#fff;display:block"></i></div>
  <h5 style="margin-top:10px">Social Media</h5>
  <div style="display:flex;gap:32px"><i style="width:26px;height:26px;border-radius:50%;background:#fff;display:block"></i><i style="width:26px;height:26px;border-radius:50%;background:#fff;display:block"></i><i style="width:26px;height:26px;border-radius:50%;background:#fff;display:block"></i></div>
</div>
<div class="abs" style="left:0;top:4622px;width:1200px;text-align:center;color:#fff;font-size:10px">© 2023 Auental Agrarhandel GbR</div>

</body>
</html>
```